Eyecatching Carpentry Business card

I need a business card designed for myself, my company name is Lewis Dunmore Carpentry.
I am based on the south coast of England and I do all aspects of carpentry, including;
skirting
Architraves
kitchens
roof construction
flooring
doors
loft conversions
decking
windows
I currently have no company logo or letter head so I leave all design ideas to designers.
All I ask is that it looks professional and modern.
A logo may be incorporated as well.
My contact details should be on the back, telephone and email.

```html
<!DOCTYPE html>
<html lang="en">
<head>
<meta charset="utf-8">
<title>Lewis Dunmore Carpentry – Business Card</title>
<link rel="stylesheet" href="https://fonts.googleapis.com/css2?family=Cormorant+Garamond:wght@500;600&family=Arimo:wght@400&display=swap">
<style>
  :root {
    --backdrop: #e9e6e1;
    --brand-blue: #0a72d1;
    --brand-blue-light: #1f8ae3;
    --accent-sky: #29b4f2;
    --accent-pale: #5ccdfc;
    --card-white: #ffffff;
    --ink: #3a3a3a;
    --ink-soft: #4a4a4a;
  }
  * { margin: 0; padding: 0; box-sizing: border-box; }
  html, body {
    width: 1200px;
    height: 800px;
    overflow: hidden;
    background: var(--backdrop);
  }
  .canvas {
    position: relative;
    width: 1200px;
    height: 800px;
    display: flex;
    align-items: center;
    justify-content: center;
    gap: 60px;
  }
  .card {
    position: relative;
    width: 500px;
    height: 290px;
    border-radius: 3px;
    box-shadow: 0 6px 18px rgba(0,0,0,0.15);
    overflow: hidden;
  }

  /* Front */
  .card--front {
    background: linear-gradient(135deg, var(--brand-blue-light) 0%, var(--brand-blue) 100%);
  }
  .front-lockup {
    position: absolute;
    left: 48px;
    top: 118px;
    display: flex;
    align-items: center;
    gap: 16px;
  }
  .front-lockup__square {
    width: 40px;
    height: 40px;
    background: var(--accent-pale);
  }
  .front-lockup__name {
    font-family: "Cormorant Garamond", Georgia, serif;
    font-weight: 600;
    font-size: 30px;
    color: var(--card-white);
    line-height: 1;
  }

  /* Back */
  .card--back {
    background: var(--card-white);
  }
  .back-lockup {
    position: absolute;
    left: 36px;
    top: 32px;
    display: flex;
    align-items: center;
    gap: 12px;
  }
  .back-lockup__square {
    width: 22px;
    height: 22px;
    background: var(--accent-sky);
  }
  .back-lockup__name {
    font-family: "Cormorant Garamond", Georgia, serif;
    font-weight: 500;
    font-size: 17px;
    letter-spacing: 0.08em;
    text-transform: uppercase;
    color: var(--ink);
  }
  .contact {
    position: absolute;
    left: 36px;
    top: 178px;
    font-family: "Arimo", Arial, sans-serif;
    font-size: 14px;
    line-height: 1.45;
    color: var(--ink);
  }
  .feature-square {
    position: absolute;
    left: 262px;
    top: 96px;
    width: 70px;
    height: 70px;
    background: var(--accent-sky);
  }
  .services {
    position: absolute;
    left: 352px;
    top: 100px;
    list-style: none;
    font-family: "Arimo", Arial, sans-serif;
    font-size: 14px;
    line-height: 1.22;
    color: var(--ink-soft);
  }
</style>
</head>
<body>
  <main class="canvas">
    <section class="card card--front" aria-label="Business card front">
      <div class="front-lockup">
        <span class="front-lockup__square"></span>
        <span class="front-lockup__name">Lewis Dunmore Carpentry</span>
      </div>
    </section>

    <section class="card card--back" aria-label="Business card back">
      <div class="back-lockup">
        <span class="back-lockup__square"></span>
        <span class="back-lockup__name">Lewis Dunmore</span>
      </div>

      <div class="contact">
        <p class="contact__phone">T: (01273) 555 0148</p>
        <p class="contact__email">e:info@lewisdunmore.co.uk</p>
      </div>

      <span class="feature-square"></span>

      <ul class="services">
        <li>kitchens</li>
        <li>roof construction</li>
        <li>flooring</li>
        <li>doors</li>
        <li>loft conversions</li>
        <li>decking</li>
        <li>windows</li>
      </ul>
    </section>
  </main>
</body>
</html>
```